7K packaging design

We are a wholesaler for Automotive Spare Parts in Jordan and Iraq market and we needs to import spare parts from China under our company private brand "7K"
The 7K brand’s product lines include Filtration, Braking Systems, Wheels, Wheel Bolts & Nuts, Shock Absorbers, Sensors, Cooling Systems, Axles and more.
The aim of the project is to unify the brand packaging across all the product lines , we will start by the brake pads then based on the approved design we will do the other products

Target Market(s)

Jordan , Iraq Market

Industry/Entity Type

Automotive spare parts

Requirements
Must have
• Name of the product :Ceramic brake pads specs : Superior stopping power Noise suppression Low Dust Technology Made in china
Nice to have
• Brake pad outline image on the box
Should not have
• Blue color

```html
<!DOCTYPE html>
<html lang="en">
<head>
<meta charset="utf-8">
<title>7K Ceramic Brake Pads – Box Dieline</title>
<link href="https://fonts.googleapis.com/css2?family=Audiowide&family=Arimo:wght@400;700&display=swap" rel="stylesheet">
<style>
  :root{
    --die:#29abe2;
    --flap:#333333;
    --red:#ff0008;
    --red-mid:#c40006;
    --red-dark:#4a0002;
    --grey-dark:#555555;
    --grey-light:#a0a0a0;
    --white:#ffffff;
    --title-font:"Audiowide", sans-serif;
    --body-font:"Arimo", Arial, sans-serif;
  }
  *{box-sizing:border-box;margin:0;padding:0}
  html,body{width:1091px;height:1200px;overflow:hidden;background:#fff}
  .dieline{position:relative;width:1091px;height:1200px}
  .panel{position:absolute;border:0.6px solid var(--die);overflow:hidden}
  .dust-flap{background:var(--flap)}
  .lid-top{background:linear-gradient(180deg,var(--red-dark) 0%,var(--red-mid) 55%,var(--red) 100%)}
  .lid-back{background:linear-gradient(135deg,var(--red-dark) 0%,var(--red-mid) 35%,var(--red) 70%)}
  .side-left{background:linear-gradient(150deg,var(--red) 0%,var(--red) 40%,var(--red-dark) 110%)}
  .side-right{background:linear-gradient(210deg,var(--red) 0%,var(--red) 40%,var(--red-dark) 110%)}
  .car-photo{background:linear-gradient(160deg,#3d3d3d 0%,#8a8a8a 45%,#6c6c6c 100%)}
  .lock-slot{position:absolute;border:0.6px solid var(--die);border-bottom:none}
  .glue-tab{position:absolute;border:0.6px solid var(--die);border-top:none;background:var(--red-dark)}
  .front{background:radial-gradient(ellipse at 30% 35%,var(--red) 0%,var(--red) 45%,#d50006 75%,var(--red-dark) 130%)}
  .brand-name{position:absolute;font-family:var(--title-font);color:var(--white);line-height:1}
  .product-title{position:absolute;font-family:var(--title-font);font-style:italic;color:var(--white);white-space:nowrap;letter-spacing:0.5px}
  .pad-outline-area{position:absolute;background:radial-gradient(ellipse at center,rgba(255,255,255,0.10),rgba(255,255,255,0) 70%)}
  .spec-row{position:absolute;display:flex;gap:14px;align-items:center}
  .spec{display:flex;align-items:center;gap:5px;color:var(--white);font-family:var(--body-font);font-size:5.6px;line-height:1.15;text-transform:uppercase}
  .spec svg{flex:none}
  .end-flap{position:absolute}
  .upside-down{transform:rotate(180deg)}
  .made-in{position:absolute;font-family:var(--body-font);font-weight:700;color:var(--white);font-size:8px;letter-spacing:0.3px}
  svg text{font-family:var(--title-font)}
</style>
</head>
<body>
<div class="dieline">

  <!-- Row 1: top dust flaps and lid tuck -->
  <div class="panel dust-flap" style="left:60px;top:61px;width:236px;height:202px"></div>
  <div class="panel lid-top" style="left:296px;top:61px;width:499px;height:202px"></div>
  <div class="panel dust-flap" style="left:795px;top:61px;width:236px;height:202px"></div>

  <!-- Row 2: inner flaps and lid -->
  <div class="panel dust-flap" style="left:60px;top:297px;width:236px;height:202px"></div>
  <div class="panel lid-back" style="left:296px;top:263px;width:499px;height:236px"></div>
  <div class="panel dust-flap" style="left:795px;top:297px;width:236px;height:202px"></div>
  <div class="lock-slot" style="left:136px;top:485px;width:84px;height:14px"></div>
  <div class="lock-slot" style="left:871px;top:485px;width:84px;height:14px"></div>

  <!-- Row 3: back side panels -->
  <div class="panel car-photo" role="img" aria-label="Black and white photo of a sports car front" style="left:60px;top:499px;width:236px;height:202px"></div>

  <div class="panel upside-down" style="left:296px;top:499px;width:499px;height:202px">
    <svg width="499" height="202" viewBox="0 0 499 202" xmlns="http://www.w3.org/2000/svg">
      <defs>
        <linearGradient id="carA" x1="0" y1="0" x2="1" y2="1"><stop offset="0" stop-color="#6b6b6b"/><stop offset="1" stop-color="#9c9c9c"/></linearGradient>
        <linearGradient id="silverA" x1="0" y1="0" x2="1" y2="0"><stop offset="0" stop-color="#6d6d6d"/><stop offset="0.5" stop-color="#f2f2f2"/><stop offset="1" stop-color="#8a8a8a"/></linearGradient>
        <linearGradient id="redA" x1="0" y1="0" x2="0" y2="1"><stop offset="0" stop-color="#ff0008"/><stop offset="0.6" stop-color="#c50006"/><stop offset="1" stop-color="#5a0003"/></linearGradient>
        <linearGradient id="bandA" x1="0" y1="0" x2="1" y2="0"><stop offset="0" stop-color="#4d4d4d"/><stop offset="1" stop-color="#a3a3a3"/></linearGradient>
      </defs>
      <polygon points="0,0 263,0 156,202 0,202" fill="url(#carA)" role="img" aria-label="Black and white photo of a sports car"/>
      <polygon points="263,0 278,0 171,202 156,202" fill="url(#silverA)"/>
      <polygon points="278,0 499,0 499,164 191,164" fill="url(#redA)" role="img" aria-label="White line outline of two brake pads"/>
      <polygon points="191,164 499,164 499,202 171,202" fill="url(#bandA)"/>
      <text x="18" y="60" font-size="46" fill="#fff">7K</text>
      <text font-size="20" font-style="italic" fill="#fff"><tspan x="17" y="128">Ceramic</tspan><tspan x="17" y="148">Brake</tspan><tspan x="17" y="168">Pads</tspan></text>
      <g fill="none" stroke="#fff" stroke-width="1.2">
        <circle cx="221" cy="183" r="11"/><circle cx="221" cy="183" r="4"/><circle cx="221" cy="183" r="1.5"/>
        <path d="M292 179h3l5-4v16l-5-4h-3z"/><path d="M303 177l4 2-4 2M303 185l4 2-4 2"/>
        <circle cx="378" cy="183" r="9" stroke-dasharray="2 2"/><circle cx="376" cy="181" r="1"/><circle cx="381" cy="186" r="1"/>
      </g>
      <g font-family="Arimo, Arial, sans-serif" font-size="6" fill="#fff">
        <text x="237" y="178" font-family="Arimo, Arial, sans-serif">SUPERIOR</text><text x="237" y="185" font-family="Arimo, Arial, sans-serif">STOPPING</text><text x="237" y="192" font-family="Arimo, Arial, sans-serif">POWER</text>
        <text x="314" y="182" font-family="Arimo, Arial, sans-serif">NOISE</text><text x="314" y="189" font-family="Arimo, Arial, sans-serif">SUPPRESSION</text>
        <text x="395" y="182" font-family="Arimo, Arial, sans-serif">LOW DUST</text><text x="395" y="189" font-family="Arimo, Arial, sans-serif">TECHNOLOGY</text>
      </g>
    </svg>
  </div>

  <div class="panel car-photo" role="img" aria-label="Black and white photo of a sports car front" style="left:795px;top:499px;width:236px;height:202px">
    <div class="upside-down" style="position:absolute;inset:0">
      <div class="brand-name" style="left:60px;top:58px;font-size:52px">7K</div>
      <div class="product-title" style="left:28px;top:145px;font-size:14px">Ceramic Brake Pads</div>
      <div class="made-in" style="left:84px;top:182px">MADE IN CHINA</div>
    </div>
  </div>

  <!-- Row 4: side panels and front face -->
  <div class="panel side-left" style="left:60px;top:701px;width:236px;height:193px"></div>
  <div class="glue-tab" style="left:132px;top:894px;width:92px;height:9px"></div>

  <div class="panel front" style="left:296px;top:701px;width:499px;height:236px">
    <div class="brand-name" style="left:24px;top:14px;font-size:56px">7K</div>
    <div class="product-title" style="left:24px;top:127px;font-size:18px">Ceramic Brake Pads</div>
    <div class="pad-outline-area" role="img" aria-label="White line outline of two brake pads" style="left:225px;top:38px;width:253px;height:160px"></div>
    <div class="spec-row" style="left:22px;top:181px">
      <div class="spec">
        <svg width="22" height="22" viewBox="0 0 22 22" fill="none" stroke="#fff" stroke-width="1.2"><circle cx="11" cy="11" r="10"/><circle cx="11" cy="11" r="4"/><circle cx="11" cy="11" r="1.5"/></svg>
        <span>Superior<br>Stopping<br>Power</span>
      </div>
      <div class="spec">
        <svg width="18" height="18" viewBox="0 0 18 18" fill="none" stroke="#fff" stroke-width="1.2"><path d="M1 6h3l5-4v14l-5-4H1z"/><path d="M12 4l4 2-4 2M12 11l4 2-4 2"/></svg>
        <span>Noise<br>Suppression</span>
      </div>
      <div class="spec">
        <svg width="20" height="20" viewBox="0 0 20 20" fill="none" stroke="#fff" stroke-width="1.2"><circle cx="10" cy="10" r="8.5" stroke-dasharray="2 2"/><circle cx="8" cy="8" r="1"/><circle cx="12" cy="13" r="1"/></svg>
        <span>Low Dust<br>Technology</span>
      </div>
    </div>
  </div>

  <div class="panel side-right" style="left:795px;top:701px;width:236px;height:193px"></div>
  <div class="glue-tab" style="left:867px;top:894px;width:93px;height:9px"></div>

  <!-- Row 5: bottom panel and end flaps -->
  <svg class="end-flap" style="left:116px;top:937px" width="181" height="203" viewBox="0 0 181 203" xmlns="http://www.w3.org/2000/svg">
    <defs><linearGradient id="flapL" x1="0" y1="0" x2="0" y2="1"><stop offset="0" stop-color="#ff0008"/><stop offset="0.5" stop-color="#e00007"/><stop offset="1" stop-color="#6a0003"/></linearGradient></defs>
    <path d="M180.5 0.5H36C12 0.5 0.5 18 0.5 48C0.5 110 56 199 108 200L180.5 202Z" fill="url(#flapL)" stroke="#29abe2" stroke-width="0.6"/>
  </svg>

  <div class="panel" style="left:296px;top:937px;width:499px;height:202px">
    <svg width="499" height="202" viewBox="0 0 499 202" xmlns="http://www.w3.org/2000/svg">
      <defs>
        <linearGradient id="carB" x1="0" y1="0" x2="1" y2="1"><stop offset="0" stop-color="#6b6b6b"/><stop offset="1" stop-color="#9c9c9c"/></linearGradient>
        <linearGradient id="silverB" x1="0" y1="0" x2="1" y2="0"><stop offset="0" stop-color="#6d6d6d"/><stop offset="0.5" stop-color="#f2f2f2"/><stop offset="1" stop-color="#8a8a8a"/></linearGradient>
        <linearGradient id="redB" x1="0" y1="0" x2="0" y2="1"><stop offset="0" stop-color="#ff0008"/><stop offset="0.6" stop-color="#c50006"/><stop offset="1" stop-color="#5a0003"/></linearGradient>
        <linearGradient id="bandB" x1="0" y1="0" x2="1" y2="0"><stop offset="0" stop-color="#4d4d4d"/><stop offset="1" stop-color="#a3a3a3"/></linearGradient>
      </defs>
      <polygon points="0,0 263,0 156,202 0,202" fill="url(#carB)" role="img" aria-label="Black and white photo of a sports car"/>
      <polygon points="263,0 278,0 171,202 156,202" fill="url(#silverB)"/>
      <polygon points="278,0 499,0 499,164 191,164" fill="url(#redB)" role="img" aria-label="White line outline of two brake pads"/>
      <polygon points="191,164 499,164 499,202 171,202" fill="url(#bandB)"/>
      <text x="18" y="60" font-size="46" fill="#fff">7K</text>
      <text font-size="20" font-style="italic" fill="#fff"><tspan x="17" y="128">Ceramic</tspan><tspan x="17" y="148">Brake</tspan><tspan x="17" y="168">Pads</tspan></text>
      <g fill="none" stroke="#fff" stroke-width="1.2">
        <circle cx="221" cy="183" r="11"/><circle cx="221" cy="183" r="4"/><circle cx="221" cy="183" r="1.5"/>
        <path d="M292 179h3l5-4v16l-5-4h-3z"/><path d="M303 177l4 2-4 2M303 185l4 2-4 2"/>
        <circle cx="378" cy="183" r="9" stroke-dasharray="2 2"/><circle cx="376" cy="181" r="1"/><circle cx="381" cy="186" r="1"/>
      </g>
      <g font-size="6" fill="#fff">
        <text x="237" y="178" font-family="Arimo, Arial, sans-serif">SUPERIOR</text><text x="237" y="185" font-family="Arimo, Arial, sans-serif">STOPPING</text><text x="237" y="192" font-family="Arimo, Arial, sans-serif">POWER</text>
        <text x="314" y="182" font-family="Arimo, Arial, sans-serif">NOISE</text><text x="314" y="189" font-family="Arimo, Arial, sans-serif">SUPPRESSION</text>
        <text x="395" y="182" font-family="Arimo, Arial, sans-serif">LOW DUST</text><text x="395" y="189" font-family="Arimo, Arial, sans-serif">TECHNOLOGY</text>
      </g>
    </svg>
  </div>

  <svg class="end-flap" style="left:795px;top:937px" width="181" height="203" viewBox="0 0 181 203" xmlns="http://www.w3.org/2000/svg">
    <defs><linearGradient id="flapR" x1="0" y1="0" x2="0" y2="1"><stop offset="0" stop-color="#ff0008"/><stop offset="0.5" stop-color="#e00007"/><stop offset="1" stop-color="#6a0003"/></linearGradient></defs>
    <path d="M0.5 0.5H145C169 0.5 180.5 18 180.5 48C180.5 110 125 199 73 200L0.5 202Z" fill="url(#flapR)" stroke="#29abe2" stroke-width="0.6"/>
  </svg>

</div>
</body>
</html>
```